Take my logo and make me some cool looking business cards

I've got a logo that we've trademarked so you can't change the logo but you can change it's color combo and find a fun way to incorporate it into a new business card design that is fresh, stylish, and can be applied to some cool medium cost materials (plastic, wood, metal, etc). Basically, we're looking for business cards that stand out in a good way.
Updates
Here's the logo we're currently using:
Thanks to everyone that has submitted designs. We've narrowed down to the top 4 designs and tried to eliminate old versions or designs that just didn't match our vision as quickly as we could. We don't plan on keeping this open for the full 9 days; we plan on selecting a design in the next 48 hours; with the goal of having something in the hands of a printer, preferably plastic printer, by Thursday AM Pacific Time.
Industry/Entity Type
Business
Requirements
Must have
- must include our existing logo

```html
<!DOCTYPE html>
<html lang="en">
<head>
<meta charset="utf-8">
<title>Tandem Business Cards</title>
<link rel="stylesheet" href="https://fonts.googleapis.com/css2?family=Source+Sans+3:wght@400;600&display=swap">
<style>
  :root {
    --backdrop: #2e2e2e;
    --navy: #2c3d52;
    --navy-pattern: #34475f;
    --paper: #ffffff;
    --ink: #2c3d52;
  }
  * { margin: 0; padding: 0; box-sizing: border-box; }
  html, body { width: 1200px; height: 900px; overflow: hidden; }
  body {
    background: var(--backdrop);
    font-family: "Source Sans 3", sans-serif;
    position: relative;
  }
  .card {
    position: absolute;
    top: 295px;
    width: 492px;
    height: 309px;
    border-radius: 20px;
    overflow: hidden;
  }
  .card-front { left: 95px; background: var(--navy); }
  .card-back { left: 615px; background: var(--paper); color: var(--ink); }
  .brand-pattern {
    position: absolute; inset: 0;
    background: linear-gradient(135deg, var(--navy-pattern), var(--navy));
  }
  .wordmark {
    position: absolute;
    font-weight: 600;
    font-size: 30px;
    letter-spacing: 2px;
    line-height: 1;
  }
  .card-front .wordmark { right: 38px; top: 196px; color: var(--paper); }
  .card-back .wordmark { left: 32px; top: 148px; color: var(--ink); }
  .contact { position: absolute; left: 281px; top: 148px; }
  .contact-name { font-size: 19px; line-height: 1.2; }
  .contact-role { font-size: 13.5px; margin-top: 2px; }
  .contact-lines { margin-top: 12px; font-size: 13.5px; line-height: 17px; }
  .contact-line { display: flex; align-items: flex-start; gap: 4px; }
  .contact-line svg { flex: none; margin-top: 3px; fill: var(--ink); }
  .contact-line.address { margin-top: 7px; }
</style>
</head>
<body>
  <div class="card card-front">
    <div class="brand-pattern" role="img" aria-label="Repeating pattern of the brand symbol in subtle navy tones"></div>
    <div class="wordmark">TANDEM</div>
  </div>

  <div class="card card-back">
    <div class="wordmark">TANDEM</div>
    <div class="contact">
      <div class="contact-name">Jordan Mercer</div>
      <div class="contact-role">CEO</div>
      <div class="contact-lines">
        <div class="contact-line">
          <svg width="10" height="11" viewBox="0 0 10 11" aria-hidden="true"><path d="M2 0h6a1 1 0 0 1 1 1v9a1 1 0 0 1-1 1H2a1 1 0 0 1-1-1V1a1 1 0 0 1 1-1zm.5 1.5v6.5h5V1.5zM5 8.6a.7.7 0 1 0 0 1.4.7.7 0 0 0 0-1.4z"/></svg>
          <span>+1 555 210 4836</span>
        </div>
        <div class="contact-line">
          <svg width="11" height="11" viewBox="0 0 11 11" aria-hidden="true"><path d="M0 2.5h11v7H0zM0.8 3.2l4.7 3.3 4.7-3.3v.9L5.5 7.4.8 4.1z" fill-rule="evenodd"/></svg>
          <span>jm@tandemco.com</span>
        </div>
        <div class="contact-line address">
          <svg width="10" height="12" viewBox="0 0 10 12" aria-hidden="true"><path d="M5 0a4.5 4.5 0 0 1 4.5 4.5C9.5 8 5 12 5 12S.5 8 .5 4.5A4.5 4.5 0 0 1 5 0zm0 2.7a1.8 1.8 0 1 0 0 3.6 1.8 1.8 0 0 0 0-3.6z"/></svg>
          <span>48 Harbor Lane<br>Seabright, CA 95060</span>
        </div>
      </div>
    </div>
  </div>
</body>
</html>
```